Strategic Plan Notecards (4.25in x 5.5 in)

I need a design for project cards that will be handed out to the general public as part of a Strategic Planning effort for a client. I'd like the cards to be 4.25 x 5.5 so that they can be printed 4 to a US letter-size sheet of paper.

The Project title is "City of Quellmont Strategic Plan Update"
Needs to include text:

For more info, go to www.quellmontfutures.example
Take the Vision Survey at http://lnk.example/QuellmontOutlook
What do YOU want Quellmont to be?

Other variations on this text will be considered.

Target Market(s)

General Public

Font styles to use
Serif
Sans Serif

Colors

Designer to choose colors to be used in the design.

Requirements
Must have
• An interesting and fun visual appeal. Nothing stuffy. Should have a bright graphic background and interesting typefaces for the text.
Nice to have
• One of the biggest assets in the community is the Missouri River - some depiction of a river would be great.

```html
<!DOCTYPE html>
<html lang="en">
<head>
<meta charset="utf-8">
<title>City of Quellmont Strategic Plan Update</title>
<link rel="stylesheet" href="https://fonts.googleapis.com/css2?family=Anton&family=Oswald:wght@400;500&display=swap">
<style>
  :root {
    --gold: #fbc34b;
    --navy: #13375f;
    --white: #ffffff;
    --stage: #e4e4e4;
    --water: #3f86b8;
    --land: #7c8c55;
  }
  * { margin: 0; padding: 0; box-sizing: border-box; }
  html, body { width: 1054px; height: 1200px; overflow: hidden; }
  body { background: var(--stage); position: relative; }

  .card {
    position: absolute;
    left: 78px; top: 20px;
    width: 897px; height: 1160px;
    background: var(--gold);
    overflow: hidden;
  }
  .card-shapes { position: absolute; inset: 0; }

  .title-block {
    position: absolute;
    left: 38px; top: 30px;
    width: 828px; height: 294px;
    background: var(--navy);
    text-align: center;
  }
  .title-main {
    position: absolute; left: 0; right: 0; top: 68px;
    font-family: "Anton", sans-serif;
    font-size: 96px; line-height: 1;
    color: var(--gold);
    letter-spacing: 1px;
  }
  .title-main .small { font-size: 62px; margin: 0 6px; }
  .title-sub {
    position: absolute; left: 0; right: 0; top: 204px;
    font-family: "Anton", sans-serif;
    font-size: 50px; line-height: 1;
    color: var(--white);
    letter-spacing: 2px;
  }

  .question {
    position: absolute;
    left: 38px; top: 764px;
    width: 316px; height: 367px;
    background: var(--navy);
    display: flex; flex-direction: column; justify-content: center; align-items: center;
    gap: 6px;
    font-family: "Oswald", sans-serif;
    font-weight: 500;
    font-size: 58px; line-height: 1.2;
    color: var(--gold);
    letter-spacing: 2px;
    text-align: center;
  }
  .question .place {
    font-family: "Anton", sans-serif;
    font-weight: 400;
    color: var(--white);
    font-size: 54px;
    letter-spacing: 1px;
  }

  .links {
    position: absolute;
    left: 408px; top: 938px;
    width: 462px;
    text-align: center;
    color: var(--navy);
  }
  .links .lead {
    font-family: "Oswald", sans-serif;
    font-size: 28px; line-height: 1.2;
    letter-spacing: 1.5px;
  }
  .links .url {
    font-family: "Anton", sans-serif;
    font-size: 29px; line-height: 1.3;
    letter-spacing: 0.5px;
  }
  .links .divider {
    margin: 14px auto 12px;
    width: 438px;
    border-top: 2px dashed var(--navy);
  }
</style>
</head>
<body>
  <main class="card">
    <svg class="card-shapes" width="897" height="1160" viewBox="0 0 897 1160" aria-hidden="false">
      <defs>
        <linearGradient id="river-scene" x1="0" y1="0" x2="1" y2="1">
          <stop offset="0" stop-color="#6f8a5a"/>
          <stop offset="0.35" stop-color="#4c8fbf"/>
          <stop offset="0.6" stop-color="#8a9a62"/>
          <stop offset="0.8" stop-color="#3a7fb3"/>
          <stop offset="1" stop-color="#5e7046"/>
        </linearGradient>
      </defs>
      <polygon class="river-photo" role="img"
        aria-label="Aerial photograph of the river winding through wooded islands and sandbars, crossed by a highway bridge and a steel railroad bridge"
        points="0,308 866,308 866,237 897,237 897,878 0,952"
        fill="url(#river-scene)"/>
      <rect class="header-band" x="38" y="336" width="828" height="26" fill="var(--navy)"/>
      <polygon class="accent-stripe" points="354,924 897,870 897,876 354,936" fill="var(--navy)"/>
    </svg>

    <header class="title-block">
      <h1 class="title-main">CITY <span class="small">OF</span> QUELLMONT</h1>
      <h2 class="title-sub">STRATEGIC PLAN UPDATE</h2>
    </header>

    <section class="question">
      <span>WHAT DO</span>
      <span>YOU WANT</span>
      <span class="place">QUELLMONT</span>
      <span>TO BE?</span>
    </section>

    <section class="links">
      <p class="lead">Take the Vision Survey at</p>
      <p class="url">http://lnk.example/QuellmontOutlook</p>
      <div class="divider"></div>
      <p class="lead">For more info, go to</p>
      <p class="url">www.quellmontfutures.example</p>
    </section>
  </main>
</body>
</html>
```